Re-design of website: www.veltramedia.ca/en/

Veltrameda B is a promotional agency specializing in on-site marketing. We are re-designing their website.

We have already produced a prototype:
http://norvapixel.com/veltramedia_siteweb/

The architecture in the prototype must be respected. Please dress up the design with green, grey and black circles and other textures found on their current website www.veltramedia.ca

Inspiration for design that we like, clean, flat design:

- http://www.brimfoxlab.co/
- http://quellarworks.com/#!/process
- http://wearetolvane.com/

Delivrables: PSD files of each page of the prototype

Here are the images of their print portfolio: http://ftp.veltramedia.ca/clients/VLM/VELTRAMEDIA-PORTFOLIO-2012_EN.zip

Industry/Entity Type

Architecture

Requirements
Must have
• Responsive Design

```html
<!DOCTYPE html>
<html lang="fr">
<head>
<meta charset="utf-8">
<title>Veltrameda B — Agence</title>
<link rel="stylesheet" href="https://fonts.googleapis.com/css2?family=Exo+2:wght@300;400;600&family=Arimo:wght@400;700&display=swap">
<style>
  :root {
    --page-bg: #e8e8e8;
    --header-light: #ffffff;
    --header-grey: #dedede;
    --ink-dark: #2b2b2b;
    --nav-green: #a5d26f;
    --nav-active: #7eab48;
    --nav-text: #ffffff;
    --hero-dark: #262626;
    --hero-text: #f2f2f2;
    --accent-green: #a8dc5e;
    --strip-light: #f4f4f4;
    --strip-grey: #d9d9d9;
  }
  * { box-sizing: border-box; margin: 0; padding: 0; }
  html, body {
    width: 1200px;
    height: 900px;
    overflow: hidden;
    background: var(--page-bg);
  }
  .site {
    width: 1200px;
    height: 900px;
    display: flex;
    flex-direction: column;
  }
  .container {
    width: 726px;
    margin: 0 auto;
  }

  /* Header */
  .site-header {
    height: 150px;
    background: radial-gradient(ellipse at 50% 40%, var(--header-light) 0%, #f3f3f3 45%, var(--header-grey) 100%);
  }
  .site-header .container {
    height: 100%;
    display: flex;
    align-items: center;
    justify-content: space-between;
    padding-top: 8px;
  }
  .brand {
    display: flex;
    align-items: center;
    gap: 8px;
    font-family: "Exo 2", sans-serif;
    font-weight: 600;
    font-size: 21px;
    letter-spacing: 2px;
    text-transform: uppercase;
    color: var(--ink-dark);
  }
  .brand-dot {
    width: 22px;
    height: 22px;
    border-radius: 50%;
    background: var(--nav-green);
  }
  .social-links {
    display: flex;
    gap: 10px;
    list-style: none;
    margin-right: 26px;
  }
  .social-links li {
    width: 34px;
    height: 34px;
    border-radius: 50%;
    background: var(--nav-green);
  }

  /* Navigation */
  .main-nav {
    height: 58px;
    background: var(--nav-green);
  }
  .main-nav ul {
    display: flex;
    height: 58px;
    list-style: none;
  }
  .main-nav a {
    display: flex;
    align-items: center;
    height: 100%;
    padding: 0 15px;
    font-family: "Arimo", sans-serif;
    font-size: 15px;
    color: var(--nav-text);
    text-decoration: none;
    text-transform: uppercase;
  }
  .main-nav .is-active a {
    background: var(--nav-active);
    font-weight: 700;
    padding: 0 16px;
  }

  /* Hero */
  .hero {
    height: 381px;
    background: var(--hero-dark);
    display: flex;
    align-items: center;
    justify-content: center;
  }
  .hero-text {
    font-family: "Exo 2", sans-serif;
    font-weight: 400;
    font-size: 30px;
    line-height: 39px;
    color: var(--hero-text);
    text-align: center;
    padding-bottom: 10px;
  }
  .hero-text em {
    font-style: normal;
    color: var(--accent-green);
  }

  /* Lower band */
  .content-band {
    flex: 1;
    background: linear-gradient(90deg, var(--strip-grey) 0%, var(--strip-light) 30%, var(--strip-light) 70%, var(--strip-grey) 100%);
  }
</style>
</head>
<body>
  <div class="site">
    <header class="site-header">
      <div class="container">
        <div class="brand">Veltrameda B <span class="brand-dot"></span></div>
        <ul class="social-links" aria-label="Réseaux sociaux">
          <li></li>
          <li></li>
          <li></li>
        </ul>
      </div>
    </header>

    <nav class="main-nav">
      <ul class="container">
        <li class="is-active"><a href="#">Agence</a></li>
        <li><a href="#">Services</a></li>
        <li><a href="#">Réalisations</a></li>
        <li><a href="#">Événements</a></li>
        <li><a href="#">Recrutement</a></li>
        <li><a href="#">Contact</a></li>
      </ul>
    </nav>

    <section class="hero">
      <p class="hero-text">
        Lorem ipsum <em>dolor sit</em> amet, consectetur adipisicing elit,<br>
        sed do eiusmod tempor <em>incididunt</em> ut labore.
      </p>
    </section>

    <section class="content-band" role="img" aria-label="Bande claire texturée de cercles gris"></section>
  </div>
</body>
</html>
```